Wordpress Website - for cutting edge Artificial Intelligence company

We need a wordpress web site for our company Varquel.

Objective:
- To promote our software products to potential customers (e.g. large corporations)
- To promote our software products to potential partners (e.g. software makers who want to bundle our software inside their products)
- To promote our company to potential Investors (venture capital funds, angel investors, etc.)

Sample content and proposed structure can be found in the attached file.
Company logo is also attached.

The Orchid logo should only be used in the section relating to the Orchid Product (e.g. Orchid Text & Orchid Speech)

Target Market(s)

Core Target Market:
- Large corporations (e.g. Major Banks, Retailers & Pharmaceutical companies) who could buy our software

Industry/Entity Type

Software

Coding

Coded - Design and coding required

Font styles to use
Sans Serif

Colors
ffffff
ec1f27
000000
757575
dfdfdf
9bcb3c

Requirements
Must have
• Functionality:
• - Designed in Wordpress (using tools from pagebuildr.org, not hosted on pagebuildr.com)
• - Must have a user friendly CMS module for us to make updates easily
• - Must be designed to look great across different devices
• - Must be designed to look great in English and Chinese (as well as other future languages).

```html
<!DOCTYPE html>
<html lang="en">
<head>
<meta charset="utf-8">
<title>Varquel</title>
<link href="https://fonts.googleapis.com/css2?family=Roboto:ital,wght@0,400;0,500;0,700;1,400&display=swap" rel="stylesheet">
<style>
:root{
  --red:#ec1f27;
  --red-band:#f0303a;
  --black:#000;
  --ink:#222;
  --grey:#757575;
  --light:#dfdfdf;
  --white:#fff;
  --footer:#161616;
  --hero-dark:#2a0306;
}
*{margin:0;padding:0;box-sizing:border-box}
html,body{width:751px;height:1200px;overflow:hidden;background:var(--white);font-family:"Roboto",sans-serif;color:var(--ink)}
.page{position:relative;width:751px;height:1200px}
.abs{position:absolute}
.top-rule{left:0;top:0;width:751px;height:2px;background:var(--red)}
.header{left:0;top:2px;width:751px;height:56px;background:var(--white)}
.brand{display:flex;align-items:center;gap:8px;font-weight:500}
.brand-mark{width:12px;height:12px}
.brand-head{left:62px;top:16px;font-size:26px;color:var(--red)}
.brand-head .brand-mark{background:var(--red)}
.contact-row{top:13px;font-size:9.5px;color:var(--ink);display:flex;align-items:center;gap:6px}
.ring{width:18px;height:18px;border:1.5px solid var(--red);border-radius:50%;display:flex;align-items:center;justify-content:center}
.nav{left:249px;top:38px;display:flex;gap:16px;font-size:8.8px;font-weight:500;color:var(--ink)}
.hero{left:0;top:58px;width:751px;height:276px;background:radial-gradient(ellipse at 50% 45%,#b3101a 0%,#5a0509 45%,var(--hero-dark) 100%)}
.hero-title{left:0;top:140px;width:751px;text-align:center;color:var(--white);font-size:24.5px;font-weight:700;line-height:30px}
.btn{top:218px;height:30px;font-size:9.5px;font-weight:500;color:var(--white);display:flex;align-items:center;justify-content:center;letter-spacing:.3px}
.btn-demo{left:253px;width:117px;background:var(--red);border:1px solid #ff6a70}
.btn-contact{left:382px;width:117px;border:1.5px solid var(--white)}
.dots{left:351px;top:298px;display:flex;gap:4px}
.dot{width:10px;height:10px;border:1.3px solid var(--white);border-radius:50%}
.dot.on{background:var(--white)}
.section-title{left:0;width:751px;text-align:center;font-weight:700}
.news-title{top:362px;font-size:15.5px;color:var(--ink)}
.card{width:199px;height:167px;border:3px solid #eee;overflow:hidden}
.card-art{width:100%;height:100%}
.card-cap{left:0;bottom:0;width:100%;height:37px;background:rgba(15,15,20,.82);padding:5px 7px;color:var(--white)}
.card-cap h3{font-size:11px;font-weight:500}
.card-cap p{font-size:7px;margin-top:4px;color:#ddd}
.card-cap svg{position:absolute;right:8px;top:10px}
.stories{left:0;top:778px;width:751px;height:226px;background:var(--red-band)}
.stories-title{top:806px;font-size:15px;color:var(--white)}
.avatar{width:62px;height:62px;border-radius:50%;border:3px solid var(--white);background:linear-gradient(160deg,#d8d8d8,#8a8a8a)}
.quote{width:190px;text-align:center;color:var(--white)}
.quote p{font-size:7px;font-style:italic;line-height:14px}
.quote h4{font-size:6.5px;font-weight:500;margin-top:7px}
.quote span{display:block;font-size:6px;font-style:italic;margin-top:3px}
.footer{left:0;top:1004px;width:751px;height:196px;background:var(--footer);color:var(--white)}
.brand-foot{left:62px;top:1074px;font-size:29px;color:var(--white)}
.brand-foot .brand-mark{background:var(--white)}
.col-h{top:1024px;font-size:11.5px;font-weight:700}
.sep{top:1024px;width:1px;height:118px;background:#333}
.links{left:258px;top:1050px;font-size:7.5px;line-height:15px}
.news-copy{left:372px;top:1052px;font-size:7.5px;line-height:12.5px}
.email-input{left:372px;top:1084px;width:164px;height:21px;background:var(--white);color:#999;font-size:7px;padding:6px 9px}
.subscribe{left:373px;top:1117px;width:61px;height:21px;border:1.5px solid var(--white);font-size:7.5px;font-weight:700;display:flex;align-items:center;justify-content:center}
.contact-line{left:570px;font-size:7.5px;line-height:12px;display:flex;gap:10px}
.base-rule{left:44px;top:1156px;width:663px;height:1px;background:#2c2c2c}
.copy{left:62px;top:1173px;font-size:7.5px}
.social{left:567px;top:1169px;display:flex;gap:4px}
.social span{width:20px;height:20px;border:1.3px solid var(--white);border-radius:50%;display:flex;align-items:center;justify-content:center}
.social span::after{content:"";width:6px;height:6px;background:var(--white)}
</style>
</head>
<body>
<div class="page">
  <div class="abs top-rule"></div>
  <header class="abs header"></header>
  <div class="abs brand brand-head"><span class="brand-mark"></span>Varquel</div>

  <div class="abs contact-row" style="left:393px">
    <span class="ring"><svg width="9" height="9" viewBox="0 0 10 10"><path d="M2 1l2 2-1 1.3c.6 1.3 1.4 2.1 2.7 2.7L7 6l2 2-1.3 1.5C4.5 9 1 5.5.5 2.3z" fill="var(--red)"/></svg></span>1 555 010 0142
  </div>
  <div class="abs contact-row" style="left:497px">
    <span class="ring"><svg width="9" height="7" viewBox="0 0 10 7"><rect x=".5" y=".5" width="9" height="6" fill="none" stroke="var(--red)"/><path d="M.5.5L5 4 9.5.5" fill="none" stroke="var(--red)"/></svg></span>info@varquel.com
  </div>
  <div class="abs contact-row" style="left:622px;font-size:8.5px">
    <svg width="14" height="9"><rect width="14" height="9" fill="#2c3e8f"/><path d="M0 4.5h14M7 0v9" stroke="#fff" stroke-width="2.4"/><path d="M0 4.5h14M7 0v9" stroke="var(--red)" stroke-width="1.2"/></svg>ENGLISH <svg width="6" height="4"><path d="M0 0h6L3 4z" fill="var(--ink)"/></svg>
  </div>
  <nav class="abs nav">
    <span>NATURAL INTELLIGENCE</span><span>PRODUCTS</span><span>SERVICES</span><span>PARTNERS</span><span>CONTACT US</span><span>ABOUT</span>
    <svg width="9" height="9" viewBox="0 0 10 10" style="margin-left:2px"><circle cx="4" cy="4" r="3" fill="none" stroke="var(--ink)" stroke-width="1.5"/><path d="M6.3 6.3L9 9" stroke="var(--ink)" stroke-width="1.6"/></svg>
  </nav>

  <section class="abs hero" role="img" aria-label="Glowing red network of connected nodes on a dark background"></section>
  <h1 class="abs hero-title">Orchid, by Varquel. The new standard in<br>contact center customer experience</h1>
  <div class="abs btn btn-demo">REQUEST A DEMO</div>
  <div class="abs btn btn-contact">CONTACT US</div>
  <div class="abs dots"><span class="dot on"></span><span class="dot"></span><span class="dot"></span><span class="dot"></span></div>

  <h2 class="abs section-title news-title">RECENT NEWS</h2>

  <article class="abs card" style="left:62px;top:396px"><div class="card-art" role="img" aria-label="Digital head dissolving into data fragments" style="background:linear-gradient(160deg,#9fd4f0,#2f7fc4 60%,#123a63)"></div><div class="abs card-cap"><h3>Finibus Bonorum et Malorum</h3><p>▦ 13/10/2016 &nbsp;| &nbsp;● John</p><svg width="14" height="14" viewBox="0 0 14 14"><path d="M2 2l5 5-5 5M7 2l5 5-5 5" fill="none" stroke="#fff" stroke-width="1.8"/></svg></div></article>
  <article class="abs card" style="left:276px;top:396px"><div class="card-art" role="img" aria-label="Soldier wearing a smart visor with holographic interface" style="background:linear-gradient(150deg,#7a8a86,#4e5a48 55%,#9aa9ab)"></div><div class="abs card-cap"><h3>Finibus Bonorum et Malorum</h3><p>▦ 13/10/2016 &nbsp;| &nbsp;● John</p><svg width="14" height="14" viewBox="0 0 14 14"><path d="M2 2l5 5-5 5M7 2l5 5-5 5" fill="none" stroke="#fff" stroke-width="1.8"/></svg></div></article>
  <article class="abs card" style="left:490px;top:396px"><div class="card-art" role="img" aria-label="Hand holding a molecular structure model" style="background:linear-gradient(160deg,#e8eef2,#b9c8d2 60%,#8fa6b5)"></div><div class="abs card-cap"><h3>Finibus Bonorum et Malorum</h3><p>▦ 13/10/2016 &nbsp;| &nbsp;● John</p><svg width="14" height="14" viewBox="0 0 14 14"><path d="M2 2l5 5-5 5M7 2l5 5-5 5" fill="none" stroke="#fff" stroke-width="1.8"/></svg></div></article>
  <article class="abs card" style="left:62px;top:579px"><div class="card-art" role="img" aria-label="Blue abstract light streaks in motion" style="background:linear-gradient(150deg,#0b2a5a,#1c7fd6 50%,#062040)"></div><div class="abs card-cap"><h3>Finibus Bonorum et Malorum</h3><p>▦ 13/10/2016 &nbsp;| &nbsp;● John</p><svg width="14" height="14" viewBox="0 0 14 14"><path d="M2 2l5 5-5 5M7 2l5 5-5 5" fill="none" stroke="#fff" stroke-width="1.8"/></svg></div></article>
  <article class="abs card" style="left:276px;top:579px"><div class="card-art" role="img" aria-label="Hand touching a hexagon diagram about machine learning" style="background:linear-gradient(150deg,#c9d3de,#6f8fb0 55%,#3a5d86)"></div><div class="abs card-cap"><h3>Finibus Bonorum et Malorum</h3><p>▦ 13/10/2016 &nbsp;| &nbsp;● John</p><svg width="14" height="14" viewBox="0 0 14 14"><path d="M2 2l5 5-5 5M7 2l5 5-5 5" fill="none" stroke="#fff" stroke-width="1.8"/></svg></div></article>
  <article class="abs card" style="left:490px;top:579px"><div class="card-art" role="img" aria-label="Program source code on a blue screen" style="background:linear-gradient(150deg,#1a3fa0,#0f2a78 55%,#2c5fd0)"></div><div class="abs card-cap"><h3>Finibus Bonorum et Malorum</h3><p>▦ 13/10/2016 &nbsp;| &nbsp;● John</p><svg width="14" height="14" viewBox="0 0 14 14"><path d="M2 2l5 5-5 5M7 2l5 5-5 5" fill="none" stroke="#fff" stroke-width="1.8"/></svg></div></article>

  <section class="abs stories"></section>
  <h2 class="abs section-title stories-title">SUCCESS STORIES FROM OUR PARTNERS</h2>

  <div class="abs avatar" role="img" aria-label="Portrait of Marisa Delvane" style="left:117px;top:842px"></div>
  <div class="abs quote" style="left:53px;top:908px"><p>At vero eos et accusamus et iusto odio dignissimos ducimus qui blanditiis praesentium voluptatum deleniti atque corrupti quos dolores et quas mo</p><h4>MARISA DELVANE</h4><span>Financial Services Professional</span></div>
  <div class="abs avatar" role="img" aria-label="Portrait of Tobias R. Ferrante" style="left:344px;top:842px"></div>
  <div class="abs quote" style="left:280px;top:908px"><p>At vero eos et accusamus et iusto odio dignissimos ducimus qui blanditiis praesentium voluptatum deleniti atque corrupti quos dolores et quas mo</p><h4>TOBIAS R. FERRANTE</h4><span>National Urban Fellow at the Brookfield</span></div>
  <div class="abs avatar" role="img" aria-label="Portrait of Lena Whitcombe" style="left:566px;top:842px"></div>
  <div class="abs quote" style="left:502px;top:908px"><p>At vero eos et accusamus et iusto odio dignissimos ducimus qui blanditiis praesentium voluptatum deleniti atque corrupti quos dolores et quas mo</p><h4>LENA WHITCOMBE</h4><span>Creative Strategist | Entrepreneur &amp; Upcoming</span></div>

  <footer class="abs footer"></footer>
  <div class="abs brand brand-foot"><span class="brand-mark"></span>Varquel</div>
  <div class="abs sep" style="left:241px"></div>
  <div class="abs sep" style="left:552px"></div>
  <h3 class="abs col-h" style="left:258px;color:var(--white)">INFORMATION</h3>
  <div class="abs links" style="color:var(--white)">Natural Intelligence<br>Products<br>Services<br>Partners<br>Contact Us<br>About</div>
  <h3 class="abs col-h" style="left:372px;color:var(--white)">NEWSLETTER</h3>
  <div class="abs news-copy" style="color:var(--white)">Register your email address to get<br>information about us</div>
  <div class="abs email-input">Email Address</div>
  <div class="abs subscribe" style="color:var(--white)">SUBSCRIBE</div>
  <h3 class="abs col-h" style="left:570px;color:var(--white)">CONTACT US</h3>
  <div class="abs contact-line" style="top:1054px;color:var(--white)"><svg width="7" height="9" viewBox="0 0 7 9"><path d="M3.5 9S0 5 0 3.5a3.5 3.5 0 017 0C7 5 3.5 9 3.5 9z" fill="#fff"/><circle cx="3.5" cy="3.5" r="1.2" fill="var(--footer)"/></svg><span>18 Larkmoor Ave., #205<br>Halden, ON &nbsp;Canada K2P 7L1</span></div>
  <div class="abs contact-line" style="top:1091px;color:var(--white)"><svg width="8" height="8" viewBox="0 0 10 10"><path d="M2 1l2 2-1 1.3c.6 1.3 1.4 2.1 2.7 2.7L7 6l2 2-1.3 1.5C4.5 9 1 5.5.5 2.3z" fill="#fff"/></svg><span>1 555 010 0142</span></div>
  <div class="abs contact-line" style="top:1116px;color:var(--white)"><svg width="9" height="7" viewBox="0 0 10 7"><rect width="10" height="7" fill="#fff"/><path d="M0 0l5 4 5-4" fill="none" stroke="var(--footer)"/></svg><span>info@varquel.com</span></div>
  <div class="abs base-rule"></div>
  <div class="abs copy" style="color:var(--white)">Copyrights ©2016, Varquel. All rights reserved.</div>
  <div class="abs social" aria-label="Social links"><span></span><span></span><span></span><span></span><span></span></div>
</div>
</body>
</html>
```